Eye catching while remaining subtle, stylish and professional

Pellmore Works are a Heatpump and Air Conditioning Company. I would like stationary that would be suitable to use for letters, quoting invoicing. The final design should communicate a trade/service type industry that is clean and professional

I would like the designer to also offer a Business card option as well.

Details should include company logo as attached. Company details. Name, Address, Phone, Email and Website. You can use generic details until a final design is chosen

Target Market(s)

Trade/Service Industry

Industry/Entity Type

Air Conditioning

Requirements
Must have
• LOGO, Company contact details
Nice to have
• Watermark

```html
<!DOCTYPE html>
<html lang="en">
<head>
<meta charset="utf-8">
<title>Pellmore Works – Stationery</title>
<link href="https://fonts.googleapis.com/css2?family=Arimo:wght@400;700&family=Montserrat:wght@600&display=swap" rel="stylesheet">
<style>
  :root{
    --bg:#ededed;
    --paper:#ffffff;
    --blue:#3cb3e4;
    --blue-light:#a9dff5;
    --swoosh:#c9c9c9;
    --ink:#333333;
    --ink-soft:#666666;
  }
  *{box-sizing:border-box;margin:0;padding:0}
  html,body{width:1200px;height:937px;overflow:hidden;background:var(--bg)}
  body{position:relative;font-family:"Arimo",Arial,sans-serif;color:var(--ink)}
  .sheet{position:absolute;background:var(--paper);overflow:hidden;box-shadow:0 2px 8px rgba(0,0,0,.12)}
  .wave{position:absolute;left:0;bottom:0;width:100%;display:block}
  .brand{font-family:"Montserrat",sans-serif;font-weight:600;color:var(--blue);line-height:1.05;position:absolute;white-space:nowrap}
  .brand .sub{display:block;letter-spacing:.5em;font-size:.3em;margin-top:.15em}
  .web{position:absolute;font-family:"Montserrat",sans-serif;font-weight:600;color:#fff;letter-spacing:.14em;white-space:nowrap;z-index:2}

  /* letterhead */
  .letterhead{left:185px;top:68px;width:385px;height:544px}
  .letterhead .brand{left:51px;top:48px;font-size:15px}
  .contact{position:absolute;right:20px;top:20px;text-align:right;font-size:5px;line-height:7.4px;color:var(--ink)}
  .contact b{font-weight:700}
  .contact .ico{display:inline-block;width:4px;height:4px;border-radius:50%;background:var(--blue);margin-left:2px;vertical-align:middle}
  .letter-body{position:absolute;left:36px;top:136px;width:325px;font-size:5.2px;line-height:7.6px;color:var(--ink)}
  .letter-body p{margin-bottom:7px}
  .letter-body .gap{margin-bottom:22px}
  .signature{width:26px;height:18px;background:#e4e4e4;margin:2px 0 4px}

  /* cover */
  .cover{left:636px;top:40px;width:458px;height:576px}
  .cover .brand{left:112px;top:196px;font-size:42px}
  .cover .brand .sub{letter-spacing:.62em}
  .cover .web{left:36px;bottom:10px;font-size:10px}

  /* cards */
  .card{border-radius:8px}
  .card-front{left:45px;top:658px;width:177px;height:102px}
  .card-front .brand{left:19px;top:28px;font-size:10px}
  .card-info{position:absolute;left:103px;top:16px;font-size:3.8px;line-height:5.6px}
  .card-info .name{color:var(--blue);font-weight:700}
  .card-info .ico{display:inline-block;width:3px;height:3px;border-radius:50%;background:var(--blue);margin-right:2px;vertical-align:middle}
  .card-addr{position:absolute;left:10px;bottom:5px;color:#fff;font-size:4px;line-height:5px;font-weight:700;z-index:2}
  .card-back{left:45px;top:785px;width:177px;height:100px}
  .card-back .brand{left:89px;top:57px;font-size:11px}

  /* envelopes */
  .env-front{left:265px;top:671px;width:431px;height:209px}
  .env-front .brand{left:34px;top:42px;font-size:16px}
  .env-front .web{left:14px;bottom:10px;font-size:8.5px}
  .env-back{left:736px;top:671px;width:433px;height:209px}
  .flap{position:absolute;left:0;top:0;width:100%;height:72px;border-radius:0 0 40px 40px;background:linear-gradient(180deg,var(--blue) 0%,var(--blue-light) 100%);box-shadow:0 3px 6px rgba(0,0,0,.12)}
  .env-back .web{left:0;right:0;top:24px;text-align:center;font-size:11.5px}
</style>
</head>
<body>

<svg width="0" height="0" style="position:absolute">
  <defs>
    <linearGradient id="bandFill" x1="0" y1="0" x2="1" y2="0">
      <stop offset="0" stop-color="#3cb3e4"/>
      <stop offset=".55" stop-color="#a9dff5"/>
      <stop offset="1" stop-color="#3cb3e4"/>
    </linearGradient>
  </defs>
</svg>

<!-- letterhead -->
<section class="sheet letterhead">
  <div class="brand">PELLMORE<span class="sub">WORKS</span></div>
  <div class="contact">
    <b>14 Vance Road</b><br><b>Harlow Park HK2</b><br>
    021 555 0142<span class="ico"></span><br>
    021 555 0143<span class="ico"></span><br>
    021 555 0144<span class="ico"></span><br>
    hello@pellmoreworks.co<span class="ico"></span><br>
    www.pellmoreworks.co<span class="ico"></span>
  </div>
  <div class="letter-body">
    <p>July 2, 2012</p>
    <p><b>Dear Sir,</b><br>ABC Building, def St., Country Name</p>
    <p>Thank you for choosing us for your heating and cooling needs. This letter confirms the details of the quote discussed during our recent site visit. Our team will install a high efficiency heat pump in the main living area and service the existing ducted system. All work is carried out by licensed technicians and is covered by our full workmanship guarantee.</p>
    <p class="gap">Please review the attached quote and contact us with any questions before the agreed installation date.</p>
    <p>Once the work is complete we will provide a full invoice along with care instructions for your new system. Regular servicing keeps your unit running quietly and efficiently through every season. We recommend booking a check each autumn so your heat pump is ready for winter, and we will send a reminder when it is due.</p>
    <p>Best Regards,</p>
    <div class="signature" role="img" aria-label="Handwritten signature"></div>
    <p><b>Daniel Harwick</b><br>Director<br><br>ABC Building, def St., Country Name</p>
  </div>
  <svg class="wave" viewBox="0 0 400 80" height="75" preserveAspectRatio="none">
    <path d="M0 30 C120 0 220 5 400 10 L400 18 C230 14 130 12 0 40Z" fill="var(--swoosh)"/>
    <path d="M0 42 C140 12 240 20 400 20 L400 80 L0 80Z" fill="url(#bandFill)"/>
  </svg>
</section>

<!-- cover sheet -->
<section class="sheet cover">
  <div class="brand">PELLMORE<span class="sub">WORKS</span></div>
  <svg class="wave" viewBox="0 0 400 80" height="92" preserveAspectRatio="none">
    <path d="M0 30 C120 0 220 5 400 10 L400 18 C230 14 130 12 0 40Z" fill="var(--swoosh)"/>
    <path d="M0 42 C140 12 240 20 400 20 L400 80 L0 80Z" fill="url(#bandFill)"/>
  </svg>
  <div class="web">www.pellmoreworks.co</div>
</section>

<!-- business card front -->
<section class="sheet card card-front">
  <div class="brand">PELLMORE<span class="sub">WORKS</span></div>
  <div class="card-info">
    <span class="name">OWEN TASKER</span><br><b>Managing Director</b><br><br>
    <span class="ico"></span>021 555 0142<br>
    <span class="ico"></span>021 555 0143<br>
    <span class="ico"></span>021 555 0144<br>
    <span class="ico"></span>hello@pellmoreworks.co<br>
    <span class="ico"></span>www.pellmoreworks.co
  </div>
  <svg class="wave" viewBox="0 0 400 80" height="40" preserveAspectRatio="none">
    <path d="M0 30 C120 0 220 5 400 10 L400 18 C230 14 130 12 0 40Z" fill="var(--swoosh)"/>
    <path d="M0 42 C140 12 240 20 400 20 L400 80 L0 80Z" fill="url(#bandFill)"/>
  </svg>
  <div class="card-addr">14 Vance Road<br>Harlow Park HK2</div>
</section>

<!-- business card back -->
<section class="sheet card card-back">
  <div class="brand">PELLMORE<span class="sub">WORKS</span></div>
</section>

<!-- envelope front -->
<section class="sheet env-front">
  <div class="brand">PELLMORE<span class="sub">WORKS</span></div>
  <svg class="wave" viewBox="0 0 400 80" height="62" preserveAspectRatio="none">
    <path d="M0 30 C120 0 220 5 400 10 L400 18 C230 14 130 12 0 40Z" fill="var(--swoosh)"/>
    <path d="M0 42 C140 12 240 20 400 20 L400 80 L0 80Z" fill="url(#bandFill)"/>
  </svg>
  <div class="web">www.pellmoreworks.co</div>
</section>

<!-- envelope back -->
<section class="sheet env-back">
  <div class="flap"></div>
  <div class="web">www.pellmoreworks.co</div>
</section>

</body>
</html>
```